Business Card Design

BBQ Concessions and Event Catering
Hi! My name is Walt I am looking for a biz card design for my BBQ company:
We specialize in ribs, brisket, pulled pork, chicken
Mainly Pork Product
Colors: Dark colors, Red, Black
Flames optional
This is a mobile trailer that moves to the party!
Copper Gate is a song by Lonnie Tasker which influenced the name of my company. So I Love Blues and BBQ!
We also cater at music venues, parties, receptions etc. Anyone who needs good BBQ comes to us.

Looking forward to your designs.

Industry/Entity Type

Business

Contact Information for Business Card

Copper Gate BBQ, Walt Barcombe Owner, 2218 Dunmore Ave. LaPorte, In. 46350

```html
<!DOCTYPE html>
<html lang="en">
<head>
<meta charset="utf-8">
<title>Copper Gate BBQ – Business Card</title>
<link rel="stylesheet" href="https://fonts.googleapis.com/css2?family=Oswald:wght@700&family=Arimo:wght@400&display=swap">
<style>
  :root {
    --page-bg: #e9e9e9;
    --card-bg: #f7f7f7;
    --brand-red: #e31b23;
    --ink-black: #0d0d0d;
    --grill-tone: #3a3a3a;
    --grill-ember: #c8312b;
  }
  * { box-sizing: border-box; margin: 0; padding: 0; }
  html, body {
    width: 1200px;
    height: 864px;
    overflow: hidden;
    background: var(--page-bg);
  }
  .card {
    position: absolute;
    left: 75px;
    top: 132px;
    width: 1050px;
    height: 600px;
    background: var(--card-bg);
    overflow: hidden;
    box-shadow: 0 10px 30px rgba(0,0,0,0.15);
  }
  .side-band {
    position: absolute;
    left: 0; top: 0;
    width: 85px; height: 100%;
    background: var(--brand-red);
  }
  .side-stripe {
    position: absolute;
    top: 0; height: 100%;
    background: var(--ink-black);
  }
  .side-stripe--thick { left: 85px; width: 10px; }
  .side-stripe--thin { left: 104px; width: 6px; }
  .brand-dot {
    position: absolute;
    left: 30px; top: 80px;
    width: 150px; height: 150px;
    border-radius: 50%;
    background: var(--ink-black);
  }
  .brand-name {
    position: absolute;
    left: 196px; top: 122px;
    font-family: "Oswald", sans-serif;
    font-weight: 700;
    font-size: 50px;
    line-height: 1;
    color: var(--ink-black);
    letter-spacing: 0.3px;
    white-space: nowrap;
  }
  .grill-art {
    position: absolute;
    left: 560px; top: 200px;
    width: 96px; height: 190px;
    border-radius: 50% 50% 8px 8px / 30% 30% 8px 8px;
    background: linear-gradient(180deg, var(--grill-ember) 0%, var(--grill-tone) 45%, #9a9a9a 100%);
  }
  .contact-person {
    position: absolute;
    right: 90px; top: 80px;
    text-align: right;
    font-family: "Arimo", sans-serif;
    color: var(--ink-black);
    white-space: nowrap;
  }
  .contact-person__name { font-size: 42px; line-height: 1.1; }
  .contact-person__role { font-size: 26px; line-height: 1.15; }
  .contact-address {
    position: absolute;
    right: 70px; top: 440px;
    display: flex;
    align-items: center;
    gap: 18px;
    font-family: "Arimo", sans-serif;
    font-size: 33px;
    color: var(--ink-black);
    white-space: nowrap;
  }
  .contact-address__icon { width: 30px; height: 28px; fill: var(--brand-red); }
</style>
</head>
<body>
  <main class="card">
    <div class="side-band"></div>
    <div class="side-stripe side-stripe--thick"></div>
    <div class="side-stripe side-stripe--thin"></div>

    <div class="brand-dot"></div>
    <h1 class="brand-name">Copper Gate BBQ</h1>

    <div class="grill-art" role="img" aria-label="Illustration of a smoking kettle barbecue grill with red-hot grate on three legs"></div>

    <div class="contact-person">
      <p class="contact-person__name">Walt Barcombe</p>
      <p class="contact-person__role">Owner</p>
    </div>

    <p class="contact-address">
      <span>2218 Dunmore Ave. LaPorte, In. 46350</span>
      <svg class="contact-address__icon" viewBox="0 0 30 28" aria-hidden="true">
        <path d="M15 1 L1 14 H5 V27 H12 V19 H18 V27 H25 V14 H29 Z"/>
      </svg>
    </p>
  </main>
</body>
</html>
```